Marlow Poise & Image Consultancy

Hi, I need a brochure design for my personal styling business. I have downloaded the company logo along with the content of the services offered for the brochure. Being a colour and styling business I would been keen on having some pictures of timeless fashion or colour samples, This is not absolutely necessary just an idea. I had also thought about changing and naming the services offered with a feminine, fun interesting type of theme. This may make it more inviting, I would be really interested in any of your creative ideas in this area. I will be deciding on the business card design in the next couple of days. I will download the design for this once I have made the decision. I will be okay to pay for any photo images that may be required if the brochure is selected. I had envisaged a tri fold brochure standard letter size with two folds (8.5" by 11inchs) however I am open to any suggestions. Please feel free to make any changes or modification's to the content, font etc in the files downloaded for the brochure. Many Thanks.
Updates
Project Deadline Extended
Reason: I need to extend the time for this project as I do not have all of content required for the brochure confirmed. Many Thanks
Industry/Entity Type
Fashion
Font styles to use
Look and feel
Each slider illustrates characteristics of the customer's brand and the style your logo design should communicate.

```html
<!DOCTYPE html>
<html lang="en">
<head>
<meta charset="utf-8">
<title>Marlow Poise &amp; Image Consultancy – Brochure Cover</title>
<link rel="stylesheet" href="https://fonts.googleapis.com/css2?family=Kalam:wght@700&family=Open+Sans:wght@700&display=swap">
<style>
  :root {
    --backdrop: #ebebeb;
    --panel-black: #1c1b1b;
    --accent-gold: #a88a2c;
    --headline-white: #f4f4f4;
    --headline-pink: #e0287f;
    --brand-grey: #8c9296;
    --photo-light: #d9d2c6;
    --photo-mid: #b7a08a;
    --photo-warm: #9a6a55;
  }
  html, body {
    margin: 0;
    width: 1200px;
    height: 1200px;
    overflow: hidden;
    background: var(--backdrop);
  }
  .brochure-cover {
    position: absolute;
    left: 360px;
    top: 50px;
    width: 480px;
    height: 1100px;
    box-shadow: 0 6px 24px rgba(0,0,0,0.18);
    overflow: hidden;
  }
  .cover-art {
    position: absolute;
    inset: 0;
    display: block;
  }
  .headline {
    position: absolute;
    left: 0;
    right: 0;
    top: 540px;
    margin: 0;
    text-align: center;
    font-family: "Kalam", cursive;
    font-weight: 700;
    font-size: 66px;
    line-height: 1.02;
    color: var(--headline-white);
  }
  .headline .headline-accent {
    display: block;
    color: var(--headline-pink);
  }
  .brand-lockup {
    position: absolute;
    left: 70px;
    right: 40px;
    top: 860px;
    display: flex;
    align-items: center;
    gap: 18px;
  }
  .brand-dot {
    flex: none;
    width: 44px;
    height: 44px;
    border-radius: 50%;
    background: var(--accent-gold);
  }
  .brand-name {
    margin: 0;
    font-family: "Open Sans", sans-serif;
    font-weight: 700;
    font-size: 30px;
    line-height: 1.15;
    color: var(--brand-grey);
  }
</style>
</head>
<body>
  <section class="brochure-cover">
    <svg class="cover-art" width="480" height="1100" viewBox="0 0 480 1100" aria-hidden="false">
      <defs>
        <linearGradient id="street-photo-tones" x1="0" y1="0" x2="1" y2="1">
          <stop offset="0" stop-color="var(--photo-light)"/>
          <stop offset="0.55" stop-color="var(--photo-mid)"/>
          <stop offset="1" stop-color="var(--photo-warm)"/>
        </linearGradient>
      </defs>
      <rect class="cover-photo" x="0" y="0" width="480" height="520" fill="url(#street-photo-tones)"
            role="img" aria-label="Photo of a stylish woman in a red top and striped skirt walking down a city street with a tan handbag"/>
      <path class="cover-dark-field" d="M0,500 C120,470 200,420 300,418 C380,416 440,398 480,380 L480,1100 L0,1100 Z"
            fill="var(--panel-black)"/>
      <path class="cover-wave-rule" d="M0,500 C120,470 200,420 300,418 C380,416 440,398 480,380"
            fill="none" stroke="var(--accent-gold)" stroke-width="7"/>
    </svg>

    <h1 class="headline">Dress for<br>the life you<span class="headline-accent">love</span></h1>

    <div class="brand-lockup">
      <span class="brand-dot"></span>
      <p class="brand-name">Marlow Poise &amp; Image Consultancy</p>
    </div>
  </section>
</body>
</html>
```